Venture Capital Investment Firm

We are looking to overhaul our existing website (substantially), with only using the same logos (which we can provide).
We are an investment firm that focuses on making loans to late stage technology companies. Our site should ultimately look like other venture capital firms, and look modern and fresh. We have an existing website www.northvaleloan.com which this will be replacing, although we will be using a lot of the existing written content, and potentially the numbers of pages we will need, we are not wed to anything else. Please feel free to shoot any questions at any time and thank you in advance for your help!
Websites we like as examples:
https://www.tkbrandel.com/
https://www.emberwoodfunds.com/
Target Market(s)
Potential investors who will invest in our firm, as well as potentially companies that are looking to borrow money from us.

```html
<!DOCTYPE html>
<html lang="en">
<head>
<meta charset="utf-8">
<title>Northvale Investment Partners</title>
<link href="https://fonts.googleapis.com/css2?family=Josefin+Sans:wght@400;600;700&family=Montserrat:wght@400;500;600;700&family=Roboto:wght@400&display=swap" rel="stylesheet">
<style>
:root{
  --red:#ed1c24;
  --grey:#d0d0d0;
  --navy:#13132b;
  --ink:#2a2a33;
  --text:#3a3a3a;
  --white:#ffffff;
}
*{box-sizing:border-box;margin:0;padding:0}
html,body{width:1200px;height:3749px;overflow:hidden}
body{position:relative;background:var(--grey);font-family:"Josefin Sans",sans-serif;color:var(--text)}
.abs{position:absolute}
a{color:inherit}

/* header */
.site-header{left:0;top:0;width:1200px;height:76px;background:var(--white);border-bottom:2px solid #bdbdbd}
.brand{left:73px;top:14px;display:flex;align-items:center;gap:12px;font-family:"Montserrat",sans-serif;color:var(--navy)}
.brand-dot{width:34px;height:34px;border-radius:50%;background:var(--navy)}
.brand-name{font-size:25px;font-weight:500;letter-spacing:1px;line-height:1}
.brand-sub{font-size:7.5px;font-weight:600;letter-spacing:.5px;display:block;margin-top:3px}
.nav{left:356px;top:28px;display:flex;gap:0;font-family:"Montserrat",sans-serif;font-size:15px;color:var(--red);letter-spacing:.5px}
.nav span{margin-right:37px}
.btn{display:flex;align-items:center;justify-content:center;font-family:"Montserrat",sans-serif;font-weight:500;border-radius:5px;letter-spacing:.5px}
.btn-red{background:var(--red);color:var(--white)}
.btn-outline{border:2px solid var(--red);color:var(--red)}
.contact-btn{left:983px;top:18px;width:142px;height:38px;font-size:13px}

/* hero */
.hero{left:0;top:77px;width:1200px;height:600px;background:linear-gradient(180deg,#3d4656 0%,#5a5f6d 40%,#3a3f4a 75%,#2c3038 100%)}
.hero-title{left:73px;top:222px;width:800px;font-family:"Montserrat",sans-serif;font-size:28px;font-weight:400;color:var(--white);line-height:54px;letter-spacing:.5px}
.hero-text{left:73px;top:397px;width:820px;font-family:"Montserrat",sans-serif;font-size:13.2px;color:var(--white);line-height:27px}
.hero-about{left:73px;top:558px;width:184px;height:46px;font-size:13px}
.hero-strategy{left:284px;top:558px;width:183px;height:46px;font-size:13px}

/* callback */
.callback{left:649px;top:595px;width:476px;height:654px;background:var(--white);border:2px solid var(--red)}
.callback-head{left:0;top:0;width:472px;height:108px;background:var(--red);color:var(--white);font-size:32px;font-weight:700;display:flex;align-items:center;justify-content:center;letter-spacing:1px}
.field{left:40px;width:394px;height:51px;border:2px solid #333;font-family:"Montserrat",sans-serif;font-size:17px;color:#666;padding:14px 23px}
.submit{left:113px;top:542px;width:248px;height:51px;font-size:19px;border-radius:8px}

/* features */
.feature{width:240px}
.feature-icon{position:absolute;left:0;top:0}
.feature-title{position:absolute;left:69px;top:0;font-family:"Montserrat",sans-serif;font-size:19px;font-weight:600;color:var(--red);white-space:nowrap}
.feature-text{position:absolute;left:69px;top:25px;width:190px;font-size:13px;line-height:27px;color:#444}

/* experience */
.section-title{font-family:"Montserrat",sans-serif;font-size:30px;font-weight:700;color:var(--red);letter-spacing:1px}
.exp-card{width:263px;height:263px;background:var(--white);box-shadow:0 2px 6px rgba(0,0,0,.2)}
.exp-card svg{position:absolute;left:50%;transform:translateX(-50%)}
.exp-label{position:absolute;left:0;width:263px;text-align:center;font-family:"Montserrat",sans-serif;font-size:17px;font-weight:500;color:#333;line-height:36px;letter-spacing:.8px}
.arrow-btn{font-size:13px;gap:12px;border-radius:5px}

/* testimonial */
.testi-photo{left:75px;top:1745px;width:489px;height:588px;border:3px solid var(--red);background:linear-gradient(160deg,#8a6f62,#4a3b38 55%,#2d2a2c)}
.testi-box{left:564px;top:1784px;width:563px;height:510px;background:var(--white);border:2px solid var(--red);border-left:none}
.testi-title{left:0;top:24px;width:563px;text-align:center;font-family:"Montserrat",sans-serif;font-size:28px;font-weight:600;color:var(--red);letter-spacing:1px}
.testi-quote{left:64px;top:100px;width:450px;font-family:"Roboto",sans-serif;font-size:17px;line-height:27px;color:#333}
.quote-mark{font-family:Georgia,serif;font-size:56px;color:#333;line-height:1;font-style:italic}
.avatar{left:174px;top:250px;width:104px;height:104px;border-radius:50%;border:3px solid var(--red);background:linear-gradient(180deg,#e6d8cf,#c5a898)}
.stars{left:294px;top:262px;color:#f2b01e;font-size:18px;letter-spacing:1px}
.person{left:294px;top:284px;font-family:"Roboto",sans-serif;font-size:22px;color:#1d2a6b}
.person small{display:block;font-size:16px;color:#333;margin-top:2px}

/* news */
.news-panel{left:75px;top:2407px;width:1050px;height:593px;background:var(--white)}
.news-card{width:262px;height:338px;background:var(--white);border-radius:14px;box-shadow:0 1px 8px rgba(0,0,0,.18);overflow:hidden}
.news-meta{position:absolute;top:14px;left:0;width:262px;display:flex;justify-content:center;gap:30px;font-size:12.5px;color:#1d2a6b}
.news-title{position:absolute;top:54px;left:10px;width:242px;text-align:center;font-family:"Montserrat",sans-serif;font-size:18px;font-weight:700;color:var(--red);line-height:27px}
.news-body{position:absolute;top:160px;left:18px;width:226px;text-align:center;font-size:12px;line-height:18px;color:#444}
.news-more{position:absolute;left:0;bottom:0;width:262px;height:51px;background:var(--red);color:var(--white);display:flex;align-items:center;justify-content:center;font-weight:700;font-size:14px;letter-spacing:.8px}

/* footer */
.footer{left:0;top:3129px;width:1200px;height:620px;background:var(--navy);color:var(--white)}
.foot-head{font-family:"Montserrat",sans-serif;font-size:21px;font-weight:600;letter-spacing:1px}
.foot-text{font-family:"Montserrat",sans-serif;font-size:12px;line-height:54px;letter-spacing:.3px}
.foot-links{font-family:"Montserrat",sans-serif;font-size:13px;line-height:54px;text-decoration:underline;letter-spacing:.5px}
.social{width:38px;height:38px;border-radius:50%;background:var(--white)}
.foot-brand{left:690px;top:3385px;display:flex;align-items:center;gap:22px}
.foot-brand .brand-dot{width:62px;height:62px;background:var(--white)}
.foot-brand .name{font-family:"Montserrat",sans-serif;font-size:46px;font-weight:500;line-height:1;letter-spacing:1px}
.foot-brand .sub{font-family:"Montserrat",sans-serif;font-size:14px;font-weight:600;letter-spacing:.5px;display:block;margin-top:6px;text-align:right}
.copyright{left:688px;top:3600px;font-family:"Montserrat",sans-serif;font-size:12px;text-decoration:underline;letter-spacing:.3px}
</style>
</head>
<body>

<header class="abs site-header">
  <div class="abs brand">
    <span class="brand-dot"></span>
    <div><span class="brand-name">NORTHVALE</span><span class="brand-sub">INVESTMENT PARTNERS, LLC</span></div>
  </div>
  <nav class="abs nav"><span>HOME</span><span>STRATEGY</span><span>ABOUT US</span><span>TEAM</span><span>NEWS</span><span>INVESTORS</span></nav>
  <div class="abs btn btn-red contact-btn">CONTACT US</div>
</header>

<section class="abs hero" role="img" aria-label="Dusk skyline of glass skyscrapers in a financial district"></section>
<h1 class="abs hero-title">WE ARE A GLOBAL STRUCTURED CREDIT INVESTMENT FIRM FOCUSED ON THE HEALTHCARE AND TECHNOLOGY INDUSTRIES</h1>
<p class="abs hero-text">NORTHVALE IS A PRIVATE INVESTMENT FIRM UNIQUE IN ITS DUAL FOCUS ON LIFE SCIENCE AND TECHNOLOGY CREDIT OPPORTUNITIES. OUR AMBIDEXTROUS APPROACH TO INVESTING REFLECTS A BROAD RECOGNITION AND APPRECIATION FOR THE CRITICAL ROLE INTELLECTUAL PROPERTY PLAYS IN THE SUCCESSFUL COMMERCIALIZATION OF PRODUCTS. WE APPLY OUR EXTENSIVE INDUSTRY EXPERTISE TO ASSESS THE REVENUE VISIBILITY CREATED BY THESE ASSETS AND OFFER A RANGE OF CREATIVE FINANCING SOLUTIONS.</p>
<div class="abs btn btn-red hero-about">ABOUT US</div>
<div class="abs btn btn-outline hero-strategy">OUR STRATEGY</div>

<form class="abs callback">
  <div class="abs callback-head">Get a Callback</div>
  <div class="abs field" style="top:166px">YOUR NAME</div>
  <div class="abs field" style="top:244px">YOUR EMAIL ADRESS</div>
  <div class="abs field" style="top:322px">CONTACT NUMBER</div>
  <div class="abs field" style="top:401px;height:112px">MESSAGE(OPTIONAL)</div>
  <div class="abs btn btn-red submit">SUBMIT</div>
</form>

<!-- features -->
<div class="abs feature" style="left:73px;top:722px">
  <svg class="feature-icon" width="62" height="62" viewBox="0 0 62 62" fill="none" stroke="#222" stroke-width="2"><rect x="4" y="6" width="54" height="36"/><path d="M14 32l10-12 10 8 14-14M20 42l-6 16M42 42l6 16"/></svg>
  <div class="feature-title">UNIQUE STRATEGY</div>
  <p class="feature-text">Our ambidextrous approach to investing reflects a broad recognition and appreciation for the critical role intellectual property plays in the successful commercialization</p>
</div>
<div class="abs feature" style="left:373px;top:722px">
  <svg class="feature-icon" width="62" height="62" viewBox="0 0 62 62" fill="none" stroke="#222" stroke-width="2"><circle cx="42" cy="20" r="14"/><path d="M42 12v8l6 4"/><circle cx="20" cy="34" r="8"/><path d="M6 58c0-10 6-14 14-14s14 4 14 14z"/></svg>
  <div class="feature-title">VAST EXPEREINCE</div>
  <p class="feature-text">Our ambidextrous approach to investing reflects a broad recognition and appreciation for the critical role intellectual property plays in the successful commercialization</p>
</div>
<div class="abs feature" style="left:73px;top:981px">
  <svg class="feature-icon" width="62" height="62" viewBox="0 0 62 62" fill="none" stroke="#222" stroke-width="2"><circle cx="14" cy="14" r="6"/><circle cx="31" cy="10" r="6"/><circle cx="48" cy="14" r="6"/><path d="M6 58V26h16v32M23 58V22h16v36M40 58V26h16v32"/></svg>
  <div class="feature-title">EXPERT TEAM.</div>
  <p class="feature-text">Our ambidextrous approach to investing reflects a broad recognition and appreciation for the critical role intellectual property plays in the successful commercialization</p>
</div>
<div class="abs feature" style="left:373px;top:981px">
  <svg class="feature-icon" width="62" height="62" viewBox="0 0 62 62" fill="none" stroke="#222" stroke-width="2"><circle cx="46" cy="12" r="9"/><path d="M4 58h56M8 58V44h8v14M20 58V36h8v14M32 58V30h8v28M44 58V26h8v32M6 38l20-14 10 6 12-10"/></svg>
  <div class="feature-title">SAFE INVESTMENT</div>
  <p class="feature-text">Our ambidextrous approach to investing reflects a broad recognition and appreciation for the critical role intellectual property plays in the successful commercialization</p>
</div>

<h2 class="abs section-title" style="left:73px;top:1253px">OUR EXPERIENCE</h2>

<div class="abs exp-card" style="left:138px;top:1344px">
  <svg style="top:36px" width="80" height="80" viewBox="0 0 80 80" fill="none" stroke="#ed1c24" stroke-width="2.5"><path d="M40 2v8M30 4l3 7M50 4l-3 7"/><circle cx="40" cy="32" r="16"/><path d="M45 25c-2-3-10-3-10 2s10 3 10 8-8 5-11 2M40 20v24"/><path d="M4 56h14l16 8h24l18-12c-4-4-8-4-12-2l-14 8M18 56v18H4"/></svg>
  <div class="exp-label" style="top:152px">OVER $1.2B INVESTED<br><span style="display:block;margin-top:18px">BY OUR PARTNERS.</span></div>
</div>
<div class="abs exp-card" style="left:469px;top:1344px">
  <svg style="top:44px" width="90" height="90" viewBox="0 0 90 90" fill="none" stroke="#ed1c24" stroke-width="2.5"><ellipse cx="45" cy="45" rx="42" ry="15"/><ellipse cx="45" cy="45" rx="42" ry="15" transform="rotate(60 45 45)"/><ellipse cx="45" cy="45" rx="42" ry="15" transform="rotate(120 45 45)"/><circle cx="45" cy="45" r="6"/></svg>
  <div class="exp-label" style="top:148px">40+ LIFE SCIENCE<br>&amp; TECHNOLOGY<br>INVESTMENTS</div>
</div>
<div class="abs exp-card" style="left:800px;top:1344px">
  <svg style="top:36px" width="96" height="94" viewBox="0 0 96 94" fill="none" stroke="#ed1c24" stroke-width="2.5"><circle cx="68" cy="16" r="13"/><path d="M72 10c-2-2-8-2-8 2s8 2 8 6-6 4-9 1M68 6v20"/><path d="M4 58l22-18 12 10 16-14M6 92V62h30v30M44 92V40h34v52M12 70h8M24 70h8M12 80h8M24 80h8M50 52h8M64 52h8M50 64h8M64 64h8M50 76h8M64 76h8"/></svg>
  <div class="exp-label" style="top:148px">OVER A DECADE<br>INNOVATING<br>FINANCING STRUCTURES</div>
</div>

<div class="abs btn btn-red arrow-btn" style="left:138px;top:1640px;width:253px;height:48px">MEET OUR TEAM
  <svg width="44" height="14" viewBox="0 0 44 14" fill="none" stroke="#fff" stroke-width="2"><path d="M0 7h42M36 1l6 6-6 6"/></svg></div>

<!-- testimonial -->
<div class="abs testi-photo" role="img" aria-label="Busy stock exchange trading floor with rows of monitors"></div>
<section class="abs testi-box">
  <h2 class="abs testi-title">TESTIMONIAL'S</h2>
  <span class="abs quote-mark" style="left:30px;top:80px">“</span>
  <p class="abs testi-quote">Lorem ipsum dolor sit amet, consectetur adipiscing elit, sed do eiusmod tempor incididunt ut labore et dolore magna aliqua. Quis ipsum suspendisse ultrices gravida. Risus commodo viverra maecenas accumsan lacus vel facilisis.</p>
  <span class="abs quote-mark" style="left:518px;top:210px">”</span>
  <div class="abs avatar" role="img" aria-label="Client portrait"></div>
  <div class="abs stars">★★★★</div>
  <div class="abs person">JOHN DOE<small>NYC, USA</small></div>
  <svg class="abs" style="left:224px;top:416px" width="124" height="58" viewBox="0 0 124 58" fill="none" stroke="#ed1c24" stroke-width="5"><path d="M28 3L4 29l24 26M96 3l24 26-24 26"/><g fill="#333" stroke="none"><circle cx="50" cy="29" r="4"/><circle cx="62" cy="29" r="4"/><circle cx="74" cy="29" r="4"/></g></svg>
</section>

<!-- news -->
<svg class="abs" style="left:55px;top:2385px" width="84" height="84" viewBox="0 0 84 84" fill="none" stroke="#ed1c24" stroke-width="6"><path d="M3 84V3h81"/></svg>
<svg class="abs" style="left:1064px;top:2942px" width="84" height="84" viewBox="0 0 84 84" fill="none" stroke="#ed1c24" stroke-width="6"><path d="M0 81h81V0"/></svg>
<section class="abs news-panel">
  <h2 class="abs section-title" style="left:19px;top:36px">NORTHVALE NEWS</h2>
  <article class="abs news-card" style="left:59px;top:108px">
    <div class="news-meta"><span>APRIL - 2018</span><span>Press Release</span></div>
    <h3 class="news-title">Northvale completes structured debt investment in Brightpath</h3>
    <p class="news-body">Northvale Investment Partners ("Northvale") announced today that it has completed a structured debt investment in Brightpath, Inc. ("Brightpath"), the leader in employee communication.</p>
    <div class="news-more">read full article</div>
  </article>
  <article class="abs news-card" style="left:394px;top:108px">
    <div class="news-meta"><span>OCTOBER - 2016</span><span>Press Release</span></div>
    <h3 class="news-title">Northvale completes $22,000,000 structured debt investment in Pollwise</h3>
    <p class="news-body">Northvale Investment Partners ("Northvale") announced today that it has completed a $22,000,000 structured debt investment in Pollwise AS ("Pollwise"). Pollwise, headquartered in Oslo,</p>
    <div class="news-more">read full article</div>
  </article>
  <article class="abs news-card" style="left:729px;top:108px">
    <div class="news-meta"><span>APRIL- 2016</span><span>PORTFOLIO NEWS</span></div>
    <h3 class="news-title">Halcyon Semiconductor acquired by Lumatrix for $55,000,000</h3>
    <p class="news-body">Lumatrix Optics, Inc., a leading supplier of advanced semiconductor communications components for use in Cloud connectivity, data centers, and high-speed optical and wireless networks, today announced the signing</p>
    <div class="news-more">read full article</div>
  </article>
  <div class="abs btn btn-red arrow-btn" style="left:61px;top:493px;width:253px;height:48px">READ MORE NEWS
    <svg width="44" height="14" viewBox="0 0 44 14" fill="none" stroke="#fff" stroke-width="2"><path d="M0 7h42M36 1l6 6-6 6"/></svg></div>
</section>

<!-- footer -->
<footer class="abs footer">
  <h3 class="abs foot-head" style="left:122px;top:94px">CONTACT US</h3>
  <div class="abs foot-text" style="left:121px;top:141px">GENERAL INQUIRIES<br>Please write to:&nbsp; inquiries@northvaleloan.com<br>MEDIA INQUIRIES<br>Please write to:&nbsp; media@northvaleloan.com<br>ADRESS:<br>250 Harbor Lane #402<br>San Francisco, CA&nbsp; 94107</div>
  <h3 class="abs foot-head" style="left:451px;top:94px">SITEMAP</h3>
  <div class="abs foot-links" style="left:451px;top:165px">HOME<br>STRATEGY<br>ABOUT US<br>TEAM<br>NEWS<br>INVESTORS</div>
  <span class="abs social" style="left:735px;top:102px"></span>
  <span class="abs social" style="left:825px;top:102px"></span>
  <span class="abs social" style="left:915px;top:102px"></span>
  <span class="abs social" style="left:1005px;top:102px"></span>
</footer>
<div class="abs foot-brand" style="color:#fff">
  <span class="brand-dot"></span>
  <div><span class="name">NORTHVALE</span><span class="sub">INVESTMENT PARTNERS, LLC</span></div>
</div>
<div class="abs copyright" style="color:#fff">© 2015 Northvale Investment Partners LLC.&nbsp; All Rights Reserved.</div>

</body>
</html>
```